Bold and modern Raw Manuka Honey label needed

We are needing a new label for one of our honey brands.
Raw Manuka honey has a lot of health benefits and we need a label to look appealing to health minded people but still looking like a jar of honey.
Manuka honey is a very high valued product that we export all over the world so we are looking for a clean and easy to read label as a lot of our customers are foreign and struggle with reading complex labels.
Be creative.... we have a logo and i will add it soon.
I was thinking of adding a silhouette of a bear to go with the Pell Honey name but I'm very open to anything..
Target Market(s)
Health and medical retail shops.
Industry/Entity Type
Health And Wellness
Requirements
Must have
- Brand name is "ambrel"
- Attached is our other label that we are looking at changing as well.
- Company details...
- Pell Honey NZ Limited
- 4/18 Brindle Street
- Central Auckland
- PO Box 41-582
- Auckland
- pellhoneynz@maildrop-nz.com
- www.pellhoneynz-shop.com
Nice to have
- Easy to read.
Should not have
- Hard to read fonts

```html
<!DOCTYPE html>
<html lang="en">
<head>
<meta charset="utf-8">
<title>Ambrel Manuka Honey – Jar Label</title>
<link href="https://fonts.googleapis.com/css2?family=Archivo+Black&family=Barlow:wght@400;500;600&display=swap" rel="stylesheet">
<style>
  :root {
    --backdrop: #d1d2d4;
    --paper: #ffffff;
    --honey-yellow: #ffe000;
    --charcoal: #333333;
    --ink: #1e1e1e;
  }
  * { margin: 0; padding: 0; box-sizing: border-box; }
  html, body {
    width: 1200px; height: 848px; overflow: hidden;
    background: var(--backdrop);
  }
  .canvas { position: relative; width: 1200px; height: 848px; overflow: hidden; }
  .label {
    position: absolute; left: 54px; top: 234px;
    width: 1364px; height: 475px;
    transform: scale(0.8); transform-origin: 0 0;
    background: var(--paper);
    font-family: "Barlow", Arial, sans-serif;
    color: var(--ink);
  }
  .label__band {
    position: absolute; left: 0; top: 28px; width: 100%; height: 418px;
    background: var(--honey-yellow);
  }

  .story {
    position: absolute; left: 9px; top: 98px; width: 400px;
    text-align: center; font-size: 17.5px; line-height: 20.5px;
  }
  .mgo-title {
    position: absolute; left: 65px; top: 248px;
    font-family: "Archivo Black", Arial, sans-serif;
    font-size: 19px; letter-spacing: 2.2px; font-weight: 400;
  }
  .mgo-table {
    position: absolute; left: 47px; top: 280px; width: 327px;
    border-collapse: collapse; font-size: 17.5px;
  }
  .mgo-table th {
    background: var(--charcoal); color: var(--honey-yellow);
    font-weight: 400; height: 23px; text-align: center;
  }
  .mgo-table td { height: 23.5px; text-align: center; padding: 0; line-height: 1; }
  .mgo-table .col-mgo { width: 112px; }
  .mgo-table .col-npa { width: 104px; }
  .grade-arrow { position: relative; }
  .grade-arrow svg { position: absolute; left: 50%; top: 3px; transform: translateX(-50%); }

  .product {
    position: absolute; left: 476px; top: 28px; width: 400px; height: 418px;
    text-align: center; color: var(--charcoal);
  }
  .product__type {
    position: absolute; left: 0; top: 52px; width: 100%;
    font-family: "Archivo Black", Arial, sans-serif;
    font-size: 20px; letter-spacing: 2.4px;
  }
  .product__name {
    position: absolute; left: 0; top: 82px; width: 100%;
    font-family: "Archivo Black", Arial, sans-serif; font-weight: 400;
    font-size: 62px; line-height: 76px; letter-spacing: 3px;
  }
  .product__weight {
    position: absolute; left: 100px; top: 178px; width: 200px; height: 57px;
    border-top: 1px solid var(--charcoal); border-bottom: 1px solid var(--charcoal);
    font-family: "Archivo Black", Arial, sans-serif;
    font-size: 26px; line-height: 55px;
  }
  .product__maker {
    position: absolute; left: 0; top: 362px; width: 100%;
    font-weight: 500; font-size: 14px; line-height: 16px; letter-spacing: 2px;
  }

  .nutrition {
    position: absolute; left: 1042px; top: 43px; width: 268px;
    border-collapse: collapse; font-size: 14.5px; line-height: 16.5px;
  }
  .nutrition td { border: 1px solid var(--ink); padding: 1px 3px; vertical-align: middle; }
  .nutrition .qty { text-align: center; width: 52px; padding: 1px 0; }
  .nutrition .qty-head { vertical-align: bottom; padding-bottom: 3px; }
  .nutrition__title {
    font-family: "Archivo Black", Arial, sans-serif;
    font-size: 16px; line-height: 16px; letter-spacing: 1.2px; margin: 4px 0 4px;
  }
  .nutrition .sub { padding-left: 10px; }

  .company {
    position: absolute; left: 1020px; top: 327px; width: 312px;
    text-align: center; font-size: 17.5px; line-height: 20px; font-style: normal;
  }
</style>
</head>
<body>
<main class="canvas">
  <section class="label">
    <div class="label__band"></div>

    <p class="story">Ambrel brings you 35 years of quality honey.<br>Our honeys are 100% pure natural and<br>nothing added. Honey the way it should bee.<br>Best stored at room temperature and<br>away from direct sunlight.</p>

    <h2 class="mgo-title">DIETARY MGO CONTENT</h2>
    <table class="mgo-table">
      <thead>
        <tr><th class="col-mgo">MGO</th><th class="col-npa">NPA</th><th>GRADE</th></tr>
      </thead>
      <tbody>
        <tr><td>MGO30+</td><td>2+</td><td>General</td></tr>
        <tr><td>MGO100+</td><td>5+</td>
          <td rowspan="3" class="grade-arrow">
            <svg width="12" height="62" viewBox="0 0 12 62"><line x1="6" y1="0" x2="6" y2="54" stroke="#1e1e1e" stroke-width="1.6"/><polygon points="1,53 11,53 6,61" fill="#1e1e1e"/></svg>
          </td></tr>
        <tr><td>MGO250+</td><td>10+</td></tr>
        <tr><td>MGO500+</td><td>15+</td></tr>
        <tr><td>MGO800+</td><td>20+</td><td>Premium</td></tr>
      </tbody>
    </table>

    <div class="product">
      <p class="product__type">MANUKA HONEY</p>
      <h1 class="product__name">AMBREL</h1>
      <p class="product__weight">500g</p>
      <p class="product__maker">PELL HONEY<br>NZ LIMITED</p>
    </div>

    <table class="nutrition">
      <tr>
        <td>
          <div class="nutrition__title">NUTRITIONAL<br>INFORMATION</div>
          Servings per package: 50<br>Serving size: 10g
        </td>
        <td class="qty qty-head">Qty<br>per<br>Serve</td>
        <td class="qty qty-head">Qty<br>per<br>100g</td>
      </tr>
      <tr><td>Energy</td><td class="qty">132kJ</td><td class="qty">1320kJ</td></tr>
      <tr><td>Protein</td><td class="qty">&lt;0.1g</td><td class="qty">0.4g</td></tr>
      <tr><td>Total Fat<br><span class="sub">- Saturated</span></td><td class="qty">0g<br>0g</td><td class="qty">0g<br>0g</td></tr>
      <tr><td>Carbohydrates<br><span class="sub">- Sugars</span></td><td class="qty">8.0g<br>7.8g</td><td class="qty">80g<br>78g</td></tr>
      <tr><td>Sodium</td><td class="qty">1.2mg</td><td class="qty">12mg</td></tr>
      <tr><td colspan="3">INGREDIENTS 100% Pure New Zealand Honey, Pollen.&nbsp; Certified MGO 800+</td></tr>
    </table>

    <address class="company">
      Pell Honey NZ Limited<br>
      4/18 Brindle Street, Auckland Central,<br>
      New Zealand<br>
      Export ID HIVE4&nbsp; PHB2758<br>
      Best before&nbsp; January 2019
    </address>
  </section>
</main>
</body>
</html>
```